Email Notification & Marketing Templates

I want to start with something like a newsletter or informational email, but i need Top Tips to Detect Phishing Scams. Something that i can send to users so they can follow it when receiving or exchanging emails. I will also need promotional items for my company that i can send to customers as well. It can be based on on our website PLVORIX.COM

Will also need:
newsletters
announcements
marketing emails
alerts
security notifications

Examples:Items such as Security Awareness Poster Series
Phishing Awareness
Password Security
Email Attachments
QR Code scams
Public WiFi safety

```html
<!DOCTYPE html>
<html lang="en">
<head>
<meta charset="utf-8">
<title>Stay Safe on Public WiFi – Plvorix Network Designs</title>
<link href="https://fonts.googleapis.com/css2?family=Open+Sans:wght@400;600;700;800&display=swap" rel="stylesheet">
<style>
  :root {
    --page-bg: #f3f4f3;
    --card-bg: #ffffff;
    --brand-green: #4a9a2c;
    --brand-green-light: #6cc33a;
    --headline-grey: #5d5f5e;
    --text-dark: #1c1c1c;
    --text-body: #2a2a2a;
    --footer-grey: #8c8c8c;
    --rule-grey: #dcdedd;
    --icon-grey: #c4c6c5;
    --photo-dark: #3d3a35;
    --photo-mid: #8a7d6c;
    --photo-light: #d9d2c5;
  }
  * { box-sizing: border-box; margin: 0; padding: 0; }
  html, body {
    width: 1200px; height: 933px; overflow: hidden;
    background: var(--page-bg);
    font-family: "Open Sans", Arial, sans-serif;
  }
  .email {
    position: absolute; left: 313px; top: 12px;
    width: 587px; height: 906px;
    background: var(--card-bg);
  }
  .brand {
    height: 137px;
    display: flex; align-items: center; justify-content: center; gap: 12px;
  }
  .brand-mark { width: 30px; height: 30px; background: var(--brand-green); }
  .brand-name {
    font-size: 32px; font-weight: 700; color: var(--brand-green);
    letter-spacing: 0.5px;
  }
  .rule { background: var(--rule-grey); width: 100%; }
  .rule--thin { height: 4px; }
  .rule--thick { height: 7px; }
  .headline {
    height: 80px; display: flex; align-items: center; justify-content: center;
    font-size: 39px; font-weight: 800; color: var(--headline-grey);
    letter-spacing: 0.3px;
  }
  .headline .accent { color: var(--brand-green); }
  .hero-photo {
    height: 226px;
    background:
      radial-gradient(ellipse at 40% 50%, rgba(150,200,150,0.35), transparent 45%),
      linear-gradient(90deg, var(--photo-light) 0%, var(--photo-mid) 40%, var(--photo-dark) 75%, #2f3a4a 100%);
  }
  .tips { list-style: none; padding: 18px 0 24px 28px; }
  .tips li {
    display: flex; align-items: center; gap: 11px;
    font-size: 20.5px; color: var(--text-body); height: 33.5px;
  }
  .tips svg { width: 22px; height: 22px; flex: none; }
  .promo { padding: 0 28px; }
  .promo-title {
    text-align: center; font-size: 27px; font-weight: 700; color: var(--text-dark);
    margin-top: 22px;
  }
  .promo-body { display: flex; align-items: flex-start; margin-top: 13px; }
  .promo-text {
    width: 435px; font-size: 16px; line-height: 22px; color: var(--text-body);
  }
  .service-icons {
    display: grid; grid-template-columns: 44px 44px; gap: 8px 10px; margin-left: 6px; margin-top: 0;
  }
  .service-icons svg { width: 40px; height: 36px; }
  .cta {
    display: block; width: 302px; height: 47px; margin: 27px auto 0;
    border-radius: 24px; text-align: center; line-height: 47px;
    background: linear-gradient(180deg, var(--brand-green-light), var(--brand-green));
    color: #fff; font-size: 19px; font-weight: 700; text-decoration: none;
  }
  .rule--footer { margin-top: 25px; }
  .footer {
    display: flex; justify-content: space-between; align-items: center;
    padding: 20px 28px 0 29px;
  }
  .footer-legal { font-size: 12.5px; line-height: 19px; color: var(--footer-grey); }
  .social { display: flex; gap: 8px; }
  .social span { width: 26px; height: 26px; border-radius: 50%; background: var(--icon-grey); }
</style>
</head>
<body>
  <main class="email">
    <header class="brand">
      <span class="brand-mark"></span>
      <span class="brand-name">Plvorix Network Designs</span>
    </header>
    <div class="rule rule--thin"></div>

    <h1 class="headline"><span class="accent">STAY SAFE</span>&nbsp;ON PUBLIC WIFI</h1>
    <div class="hero-photo" role="img" aria-label="Person working on a laptop in a café with a coffee cup and notebook, glowing security shield and warning icons floating above the keyboard"></div>

    <ul class="tips">
      <li><svg viewBox="0 0 22 22"><circle cx="11" cy="11" r="11" fill="#4a9a2c"/><path d="M6 11.5l3.2 3.2L16 8" fill="none" stroke="#fff" stroke-width="2.4" stroke-linecap="round" stroke-linejoin="round"/></svg>Avoid Sensitive Logins</li>
      <li><svg viewBox="0 0 22 22"><circle cx="11" cy="11" r="11" fill="#4a9a2c"/><path d="M6 11.5l3.2 3.2L16 8" fill="none" stroke="#fff" stroke-width="2.4" stroke-linecap="round" stroke-linejoin="round"/></svg>Use a Reputable VPN</li>
      <li><svg viewBox="0 0 22 22"><circle cx="11" cy="11" r="11" fill="#4a9a2c"/><path d="M6 11.5l3.2 3.2L16 8" fill="none" stroke="#fff" stroke-width="2.4" stroke-linecap="round" stroke-linejoin="round"/></svg>Verify Network Names with Staff</li>
    </ul>
    <div class="rule rule--thick"></div>

    <section class="promo">
      <h2 class="promo-title">Is Your Business Network Secure?</h2>
      <div class="promo-body">
        <p class="promo-text">While public WiFi poses personal risks, business network vulnerabilities are evre even more critical. Ensure your company's data is protected with our comprehensive cybersecurity and managed network services.</p>
        <div class="service-icons">
          <svg viewBox="0 0 40 36" fill="none" stroke="#4a9a2c" stroke-width="2"><rect x="3" y="4" width="26" height="22"/><path d="M3 11h26M3 18h26M12 4v7M20 11v7M12 18v8"/><path d="M30 20l6 2v5c0 3-3 5-6 6-3-1-6-3-6-6v-5z"/></svg>
          <svg viewBox="0 0 40 36" fill="none" stroke="#4a9a2c" stroke-width="2"><path d="M10 18a7 7 0 0 1 2-13 9 9 0 0 1 17 3 6 6 0 0 1 1 10z"/><ellipse cx="20" cy="22" rx="8" ry="3"/><path d="M12 22v8c0 2 4 3 8 3s8-1 8-3v-8M12 26c0 2 4 3 8 3s8-1 8-3"/></svg>
          <svg viewBox="0 0 40 36" fill="none" stroke="#4a9a2c" stroke-width="2"><path d="M20 2l13 5v10c0 8-6 14-13 17C13 31 7 25 7 17V7z"/><rect x="15" y="16" width="10" height="8"/><path d="M17 16v-3a3 3 0 0 1 6 0v3"/></svg>
          <svg viewBox="0 0 40 36" fill="none" stroke="#4a9a2c" stroke-width="2"><rect x="3" y="3" width="34" height="23"/><path d="M15 26v6M25 26v6M11 32h18"/><path d="M8 21l8-7 6 4 9-9"/></svg>
        </div>
      </div>
      <a class="cta" href="https://plvorix.com">PROTECT YOUR BUSINESS</a>
    </section>

    <div class="rule rule--thin rule--footer"></div>
    <footer class="footer">
      <p class="footer-legal">Plvorix Network Designs, Inc.<br>© 2022 Plvorix – Inc. All rights reserved.</p>
      <div class="social" aria-label="Social links">
        <span></span><span></span><span></span><span></span>
      </div>
    </footer>
  </main>
</body>
</html>
```